Painting Contractor Business Card Design

We are looking for a cool, bold, modern, polished, business card design. We are a high-end residential painting contractor. Please incorporate our logo and keep with our green/black color scheme. We are interested in seeing 2-sided and 1-sided options. Thank you very much!

Industry/Entity Type

Business

Contact Information for Business Card

Info for the card:
Owen Talsky
mobile 206-555-0193
email owen@kestrowfinish.net
web www.kestrowfinish.net

```html
<!DOCTYPE html>
<html lang="en">
<head>
<meta charset="utf-8">
<title>Kestrow Finish – Business Card</title>
<link rel="stylesheet" href="https://fonts.googleapis.com/css2?family=Montserrat:wght@500;600;700&family=Roboto:wght@400&display=swap">
<style>
  :root {
    --page-bg: #e6e9e6;
    --brand-green: #3aa03c;
    --card-dark-top: #3b3b3b;
    --card-dark-bottom: #1c1c1c;
    --card-light: #ffffff;
    --card-light-shade: #f1f1f1;
    --ink-dark: #1e1e1e;
    --ink-light: #f4f4f4;
    --rule-green: #9fd49f;
    --band-warm-a: #f2c619;
    --band-warm-b: #ef6a22;
    --band-mid-a: #d8e21f;
    --band-mid-b: #f4a21b;
    --band-cool-a: #2ea7d8;
    --band-cool-b: #7bc843;
  }
  * { box-sizing: border-box; margin: 0; padding: 0; }
  html, body {
    width: 1200px;
    height: 1200px;
    overflow: hidden;
    background: var(--page-bg);
  }
  .sheet {
    position: relative;
    width: 1200px;
    height: 1200px;
    display: flex;
    flex-direction: column;
    align-items: center;
    justify-content: center;
    gap: 56px;
  }
  .card {
    position: relative;
    width: 900px;
    height: 514px;
    border-radius: 56px 10px 56px 10px;
    overflow: hidden;
    box-shadow: 0 10px 30px rgba(0,0,0,0.18);
  }

  /* Front side */
  .card--front {
    background:
      radial-gradient(ellipse at 55% 60%, rgba(255,255,255,0.07), transparent 60%),
      linear-gradient(160deg, var(--card-dark-top), var(--card-dark-bottom));
    color: var(--ink-light);
  }
  .wordmark {
    position: absolute;
    left: 76px;
    top: 86px;
    display: flex;
    align-items: center;
    gap: 22px;
  }
  .wordmark__dot {
    width: 58px;
    height: 58px;
    background: var(--brand-green);
  }
  .wordmark__name {
    font-family: "Montserrat", sans-serif;
    font-weight: 600;
    font-size: 60px;
    letter-spacing: 1px;
    color: var(--brand-green);
    line-height: 1;
  }
  .holder {
    position: absolute;
    left: 90px;
    top: 272px;
    font-family: "Montserrat", sans-serif;
    font-weight: 700;
    font-size: 34px;
    letter-spacing: 1px;
    color: var(--brand-green);
    text-transform: uppercase;
  }
  .contact-list {
    position: absolute;
    left: 0;
    top: 330px;
    list-style: none;
    display: flex;
    flex-direction: column;
    gap: 16px;
  }
  .contact-list__item {
    display: flex;
    align-items: center;
    height: 34px;
  }
  .contact-list__band {
    width: 66px;
    height: 16px;
    margin-right: 12px;
  }
  .contact-list__band--warm { background: linear-gradient(90deg, var(--band-warm-a), var(--band-warm-b)); }
  .contact-list__band--mid  { background: linear-gradient(90deg, var(--band-mid-b), var(--band-mid-a)); }
  .contact-list__band--cool { background: linear-gradient(90deg, var(--band-cool-a), var(--band-cool-b)); }
  .contact-list__icon {
    width: 18px;
    height: 18px;
    margin-right: 10px;
    fill: var(--brand-green);
    flex: none;
  }
  .contact-list__text {
    font-family: "Roboto", sans-serif;
    font-size: 29px;
    color: var(--ink-light);
  }

  /* Back side */
  .card--back {
    background:
      linear-gradient(200deg, var(--card-light-shade) 0%, var(--card-light) 45%);
  }
  .lockup {
    position: absolute;
    left: 0;
    right: 0;
    top: 108px;
    display: flex;
    justify-content: center;
    align-items: center;
    gap: 30px;
  }
  .lockup__dot {
    width: 120px;
    height: 120px;
    background: var(--brand-green);
  }
  .lockup__name {
    font-family: "Montserrat", sans-serif;
    font-weight: 600;
    font-size: 92px;
    line-height: 0.98;
    letter-spacing: 3px;
    color: var(--brand-green);
  }
  .web-line {
    position: absolute;
    left: 0;
    right: 0;
    top: 360px;
    display: flex;
    justify-content: center;
    align-items: center;
    gap: 18px;
  }
  .web-line__rule {
    width: 110px;
    height: 10px;
    border-top: 3px solid var(--rule-green);
    border-bottom: 3px solid var(--rule-green);
  }
  .web-line__text {
    font-family: "Roboto", sans-serif;
    font-size: 30px;
    letter-spacing: 1px;
    color: var(--ink-dark);
  }
</style>
</head>
<body>
<main class="sheet">

  <section class="card card--front" aria-label="Business card front">
    <div class="wordmark">
      <span class="wordmark__dot"></span>
      <span class="wordmark__name">KESTROW FINISH</span>
    </div>

    <p class="holder">Owen Talsky</p>

    <ul class="contact-list">
      <li class="contact-list__item">
        <span class="contact-list__band contact-list__band--warm"></span>
        <svg class="contact-list__icon" viewBox="0 0 24 24" aria-hidden="true"><path d="M6.6 10.8a15.1 15.1 0 0 0 6.6 6.6l2.2-2.2c.3-.3.7-.4 1-.2 1.1.4 2.3.6 3.6.6.6 0 1 .4 1 1V20c0 .6-.4 1-1 1A17 17 0 0 1 3 4c0-.6.4-1 1-1h3.5c.6 0 1 .4 1 1 0 1.3.2 2.5.6 3.6.1.3 0 .7-.2 1z"/></svg>
        <span class="contact-list__text">206-555-0193</span>
      </li>
      <li class="contact-list__item">
        <span class="contact-list__band contact-list__band--mid"></span>
        <svg class="contact-list__icon" viewBox="0 0 24 24" aria-hidden="true"><path d="M2 5h20v14H2z M2 5l10 8 10-8" fill="none" stroke="#3aa03c" stroke-width="2.4"/></svg>
        <span class="contact-list__text">owen@kestrowfinish.net</span>
      </li>
      <li class="contact-list__item">
        <span class="contact-list__band contact-list__band--cool"></span>
        <svg class="contact-list__icon" viewBox="0 0 24 24" aria-hidden="true"><circle cx="12" cy="12" r="9.5" fill="none" stroke="#3aa03c" stroke-width="2.4"/><path d="M2.5 12h19M12 2.5c3 3 3 16 0 19M12 2.5c-3 3-3 16 0 19" fill="none" stroke="#3aa03c" stroke-width="1.8"/></svg>
        <span class="contact-list__text">www.kestrowfinish.net</span>
      </li>
    </ul>
  </section>

  <section class="card card--back" aria-label="Business card back">
    <div class="lockup">
      <span class="lockup__dot"></span>
      <span class="lockup__name">KESTROW<br>FINISH</span>
    </div>
    <div class="web-line">
      <span class="web-line__rule"></span>
      <span class="web-line__text">www.kestrowfinish.net</span>
      <span class="web-line__rule"></span>
    </div>
  </section>

</main>
</body>
</html>
```